Velder Auto Repair - Flyer Design

My business is a automobile shop where we fix cars. Such things that we do but not limited to is brakes, Engine/Transmission change, Electrical work, emission test, oil change and automobile diagnostic. I am looking for a flyer that will catch peoples attention, I will be giving flyers to people, putting them in car windows and mailboxes. I am looking for a flier that will help to attract more customers to my business. I also want the flyer to say "Bring in your estimate from our competitors with this flyer and we will beat it by 10%" (does not have to be in those exact words). I also want the flyer to have my business address phone and operating hours. I have attached a business card and my business ad which I have placed in the newspaper before. I hope it helps with your design.
Industry/Entity Type
Car Repair
Look and feel

```html
<!DOCTYPE html>
<html lang="en">
<head>
<meta charset="utf-8">
<title>Velder Auto Repair – Flyer</title>
<link rel="stylesheet" href="https://fonts.googleapis.com/css2?family=Bebas+Neue&family=Arimo:wght@400&family=Raleway:wght@300;700&display=swap">
<style>
  :root {
    --ink-black: #0b0b0c;
    --deep-red: #3a0a0c;
    --brand-red: #e8312f;
    --soft-red: #e5534f;
    --white: #ffffff;
    --panel-gap: #121214;
  }
  html, body {
    margin: 0;
    padding: 0;
    overflow: hidden;
    background: var(--ink-black);
  }
  .flyer {
    position: relative;
    width: 1200px;
    height: 566px;
    overflow: hidden;
    background:
      radial-gradient(ellipse 560px 240px at 420px 40px, rgba(150, 22, 26, 0.6), transparent 70%),
      linear-gradient(90deg, var(--ink-black) 0%, #161214 50%, #2a0b0d 80%, #120a0b 100%);
    color: var(--white);
  }
  .road-photo {
    position: absolute;
    left: 0;
    top: 196px;
    width: 640px;
    height: 150px;
    background:
      radial-gradient(ellipse 150px 60px at 450px 75px, rgba(40, 40, 42, 0.9), transparent 75%),
      linear-gradient(90deg, rgba(60,60,62,0) 0%, rgba(85,85,88,0.55) 40%, rgba(105,105,108,0.6) 75%, rgba(50,50,52,0.2) 100%);
    filter: blur(5px);
  }
  .photo-panels {
    position: absolute;
    inset: 0;
  }
  .brand-title {
    position: absolute;
    left: 28px;
    top: 34px;
    margin: 0;
    font-family: "Bebas Neue", sans-serif;
    font-weight: 400;
    font-size: 89px;
    line-height: 1;
    letter-spacing: 0.5px;
    white-space: nowrap;
  }
  .brand-title .brand-name { color: var(--brand-red); }
  .tagline {
    position: absolute;
    left: 36px;
    top: 114px;
    margin: 0;
    font-family: "Arimo", sans-serif;
    font-size: 33px;
    line-height: 38px;
    white-space: nowrap;
  }
  .hours {
    position: absolute;
    left: 29px;
    top: 178px;
    margin: 0;
    padding: 0;
    list-style: none;
    font-family: "Arimo", sans-serif;
    font-size: 24px;
    line-height: 27px;
    color: var(--soft-red);
    white-space: nowrap;
  }
  .offer {
    position: absolute;
    left: 28px;
    top: 301px;
    margin: 0;
    width: 380px;
    font-family: "Raleway", sans-serif;
    font-weight: 300;
    font-size: 36px;
    line-height: 38px;
  }
  .offer strong {
    font-weight: 700;
    color: var(--brand-red);
  }
  .contact {
    position: absolute;
    left: 29px;
    top: 493px;
    font-family: "Arimo", sans-serif;
    white-space: nowrap;
  }
  .contact .email { font-size: 22px; line-height: 26px; margin: 0 0 2px; }
  .contact .address { font-size: 18px; line-height: 22px; margin: 0; }
  .call-us {
    position: absolute;
    left: 810px;
    top: 44px;
    margin: 0;
    font-family: "Bebas Neue", sans-serif;
    font-size: 40px;
    line-height: 1;
    white-space: nowrap;
  }
  .call-us .label { color: var(--brand-red); }
  .call-us .divider { color: var(--brand-red); padding: 0 6px; }
</style>
</head>
<body>
  <main class="flyer">
    <div class="road-photo" role="img" aria-label="Blurred photo of a compact car driving on a road"></div>

    <svg class="photo-panels" width="1200" height="566" viewBox="0 0 1200 566">
      <defs>
        <linearGradient id="shop-base" x1="0" y1="0" x2="1" y2="1">
          <stop offset="0" stop-color="#1c1c1f"/>
          <stop offset="0.45" stop-color="#3b3d42"/>
          <stop offset="1" stop-color="#4a5058"/>
        </linearGradient>
        <radialGradient id="shop-wheel" cx="0.36" cy="0.2" r="0.32">
          <stop offset="0" stop-color="#b8babd" stop-opacity="0.8"/>
          <stop offset="0.45" stop-color="#55575b" stop-opacity="0.6"/>
          <stop offset="1" stop-color="#1a1a1c" stop-opacity="0"/>
        </radialGradient>
        <radialGradient id="shop-uniform" cx="0.82" cy="0.82" r="0.4">
          <stop offset="0" stop-color="#6f8ab3" stop-opacity="0.95"/>
          <stop offset="0.6" stop-color="#5b7398" stop-opacity="0.5"/>
          <stop offset="1" stop-color="#3b3d42" stop-opacity="0"/>
        </radialGradient>
        <linearGradient id="driver-base" x1="0" y1="0" x2="1" y2="1">
          <stop offset="0" stop-color="#2a2b2e"/>
          <stop offset="0.5" stop-color="#8f959c"/>
          <stop offset="1" stop-color="#c3c8ce"/>
        </linearGradient>
        <radialGradient id="driver-warm" cx="0.45" cy="0.42" r="0.3">
          <stop offset="0" stop-color="#c98a6a" stop-opacity="0.7"/>
          <stop offset="0.6" stop-color="#6b4a3a" stop-opacity="0.35"/>
          <stop offset="1" stop-color="#6b4a3a" stop-opacity="0"/>
        </radialGradient>
      </defs>

      <polygon points="640,200 966,566 392,566" fill="var(--panel-gap)"/>
      <polygon points="740,0 1200,0 1200,566 976,566 644,196" fill="var(--panel-gap)"/>

      <g role="img" aria-label="Photo of a smiling driver giving a thumbs up from a silver car window">
        <polygon points="638,214 956,566 402,566" fill="url(#driver-base)"/>
        <polygon points="638,214 956,566 402,566" fill="url(#driver-warm)"/>
      </g>
      <g role="img" aria-label="Photo of a mechanic in a blue uniform inspecting a car underside with a work light">
        <polygon points="746,0 1200,0 1200,566 984,566 652,200" fill="url(#shop-base)"/>
        <polygon points="746,0 1200,0 1200,566 984,566 652,200" fill="url(#shop-wheel)"/>
        <polygon points="746,0 1200,0 1200,566 984,566 652,200" fill="url(#shop-uniform)"/>
      </g>
    </svg>

    <h1 class="brand-title"><span class="brand-name">Velder</span> Auto Repair</h1>
    <p class="tagline">Specializing in Foreign &amp; Domestic cars</p>

    <ul class="hours">
      <li>Monday to Friday | 8.00 AM - 5.00 PM</li>
      <li>Saturday | 8.00 AM - 1.00 PM</li>
      <li>Sunday | CLOSED</li>
    </ul>

    <p class="offer">Bring in your estimate from our competitors with this flyer and we will beat it by <strong>10%</strong></p>

    <div class="contact">
      <p class="email">Email | VelderAutoRepair@mail.com</p>
      <p class="address">4120 S. Harbor Ave.Chicago IL. 60619</p>
    </div>

    <p class="call-us"><span class="label">Call us</span><span class="divider">|</span>(312) 555-0148</p>
  </main>
</body>
</html>
```